Machining Business Order Thank You Insert

I am looking for a business style card to include with orders that I ship. The card needs to thank the recipient for their order, and encourage them to leave a review. The card should include my business name and contact information and have an area to hand write a message.

I mainly sale on Crafvine and my own website. We are a machining an manufacturing business that are in the sale of mostly metal machined and 3d printed plastic products.

The front of the card should include the following:
Logo: (attached)
Snapgrid: https://www.instagram.com/quillforge/
Friendwall: https://www.facebook.com/QuillForge
Website: https://www.quillforge-example.com/

The back of the card needs an area to write a message

Industry/Entity Type

3D Printing, Machining, Crafvine

Contact Information for Business Card

Black or white front, white back to write a personal message

Font styles to use
Sans Serif

Colors

Designer to choose colors to be used in the design.

Requirements
Must have
• Encourage a review, social media info

```html
<!DOCTYPE html>
<html lang="en">
<head>
<meta charset="utf-8">
<title>QuillForge — Thank You Insert</title>
<link href="https://fonts.googleapis.com/css2?family=Barlow:wght@400;500;600&family=Yellowtail&display=swap" rel="stylesheet">
<style>
  :root {
    --bg: #e6e7e8;
    --paper: #ffffff;
    --ink-dark: #161616;
    --orange: #e8561f;
    --grey: #7a7a7a;
    --grey-light: #8c8c8c;
    --text-dark: #3c3c3c;
    --rule: #1a1a1a;
    --faint: #f3ece8;
  }
  * { margin: 0; padding: 0; box-sizing: border-box; }
  html, body { width: 1200px; height: 928px; overflow: hidden; }
  body {
    background: var(--bg);
    font-family: "Barlow", sans-serif;
    position: relative;
  }
  .card {
    position: absolute;
    border-radius: 16px;
    overflow: hidden;
  }
  /* Message side */
  .card--message {
    left: 267px; top: 59px; width: 670px; height: 382px;
    background: var(--paper);
  }
  .card__watermark {
    position: absolute; left: 0; right: 0; top: 150px;
    text-align: center;
    font-weight: 600; font-size: 74px; letter-spacing: 14px;
    color: var(--faint);
  }
  .write-line {
    position: absolute; left: 62px; width: 543px; height: 0;
    border-top: 2px dashed var(--rule);
  }
  .write-line--1 { top: 100px; }
  .write-line--2 { top: 190px; }
  .write-line--3 { top: 280px; }
  .card__website {
    position: absolute; left: 0; right: 0; top: 328px;
    display: flex; justify-content: center; align-items: center; gap: 8px;
    font-weight: 500; font-size: 17px; letter-spacing: 0.6px;
    color: var(--text-dark);
  }
  /* Thank-you side */
  .card--thanks {
    left: 264px; top: 484px; width: 676px; height: 386px;
    background: radial-gradient(ellipse at 60% 40%, #222 0%, var(--ink-dark) 70%);
  }
  .brand {
    position: absolute; left: 60px; top: 110px; width: 222px;
    display: flex; flex-direction: column; align-items: center; gap: 26px;
  }
  .brand__square {
    width: 96px; height: 96px;
    border: 6px solid var(--orange);
  }
  .brand__name {
    font-weight: 500; font-size: 26px; letter-spacing: 8px;
    color: var(--orange);
  }
  .thanks {
    position: absolute; left: 370px; width: 290px; text-align: center;
  }
  .thanks__title {
    top: 92px;
    font-family: "Yellowtail", cursive;
    font-size: 60px; line-height: 1;
    color: var(--orange);
  }
  .thanks__title .muted { color: var(--grey); }
  .thanks__sub {
    top: 178px;
    font-weight: 500; font-size: 27px; letter-spacing: 1.6px;
    color: var(--grey-light);
  }
  .thanks__sub .accent { color: var(--orange); font-weight: 600; }
  .thanks__review {
    top: 228px;
    font-weight: 600; font-size: 21px; letter-spacing: 1px;
    color: var(--orange);
  }
  .socials {
    position: absolute; left: 350px; width: 330px; top: 272px;
    display: flex; justify-content: center; gap: 16px;
    font-size: 18px; letter-spacing: 0.6px; color: var(--grey-light);
  }
  .social { display: flex; align-items: center; gap: 7px; }
  .social__mark {
    width: 18px; height: 18px; border-radius: 3px; background: var(--orange);
  }
</style>
</head>
<body>
  <section class="card card--message">
    <div class="card__watermark" aria-hidden="true">QUILLFORGE</div>
    <div class="write-line write-line--1"></div>
    <div class="write-line write-line--2"></div>
    <div class="write-line write-line--3"></div>
    <div class="card__website">
      <svg width="22" height="22" viewBox="0 0 22 22" aria-hidden="true">
        <circle cx="11" cy="11" r="10" fill="var(--orange)"/>
        <ellipse cx="11" cy="11" rx="4.5" ry="10" fill="none" stroke="#fff" stroke-width="1.4"/>
        <line x1="1" y1="11" x2="21" y2="11" stroke="#fff" stroke-width="1.4"/>
      </svg>
      <span>www.quillforge-example.com</span>
    </div>
  </section>

  <section class="card card--thanks">
    <div class="brand">
      <div class="brand__square"></div>
      <div class="brand__name">QUILLFORGE</div>
    </div>
    <div class="thanks thanks__title">Thank <span class="muted">You</span></div>
    <div class="thanks thanks__sub">FOR YOUR <span class="accent">ORDER</span></div>
    <div class="thanks thanks__review">Leave A Review:</div>
    <div class="socials">
      <span class="social"><span class="social__mark"></span>@quillforge</span>
      <span class="social"><span class="social__mark"></span>@QuillForge</span>
    </div>
  </section>
</body>
</html>
```